I need Business Cards and Letterhead Designed

I have a current label so I just need the template design. It should be clean and should look rich. I own a Wealth Management/Investment Advisory business and I need to brand to look substantial & mature.

The Business Cards may be one or two sided and may be a standard or non-standard size. I will likely print on very thick stock but not a requirement. Embossment or foil are also something that I may consider but is not required.
Updates

Getting some great designs, thank you all for your hard work. I have returned from a trip and will be posting individual feedback over the next day or so. In the meantime please note the following:

1st. My disclosure should be posted at the bottom or back of the card. It may be in smaller print but it must be listed as follows "all together";

Securities offered through Pelgrave Brokerage, Inc. A Registered Broker/Dealer. Member NOBKA/DEXO. Gil Prawley, Registered Representative. Advisory Services offered through Halden Brightwell an RBO Registered Investment Advisory Firm. RJV Wealth Management, Pelgrave Brokerage and Halden Brightwell are unaffiliated. CA Insurance Lic.# 0K42573

2nd. My Title should be listed as President / CEO
&
I need the following contact information included:

Address:
418 Verlow Blvd
Suite 740
Costa Mesa, CA  92626

Phone; 949-555-0173
fax: 800-555-0148
email: gil.prawley@pelgravebrokerage.com

Thank you for your help.

Best regards,

GP

Target Market(s)

Affluent Individuals & Families. C-Level Executives, Women, Accountants, Attorneys, Business Owners

Industry/Entity Type

Business

Requirements
Must have
• Both my cards and letterhead must include the following disclosure:

Securities offered through Pelgrave Brokerage, Inc. A Registered Broker/Dealer. Member NOBKA/DEXO.
Gil Prawley, Registered Representative. Advisory Services offered through Halden Brightwell an RBO Registered Investment Advisory Firm. RJV Wealth Management, Pelgrave Brokerage and Halden Brightwell are unaffiliated. CA Insurance Lic.# 0K4257
Should not have
• Do not include illustrations of money bags or gold bullion, or "$" signs or anything of that type.

```html
<!DOCTYPE html>
<html lang="en">
<head>
<meta charset="utf-8">
<title>RJV Wealth Management – Business Card</title>
<link href="https://fonts.googleapis.com/css2?family=EB+Garamond:ital,wght@0,400;0,600;0,700;1,600&family=Arimo:wght@400&display=swap" rel="stylesheet">
<style>
  :root {
    --stage: #1b1b1b;
    --paper: #ffffff;
    --teal: #1d8890;
    --teal-text: #2a9aa5;
    --teal-soft: #8cc8cc;
    --brown: #5a2616;
    --ink: #2b2b2b;
    --band: #dcc5b9;
    --footer: #b3866b;
    --shade: #cfcfcf;
  }
  * { box-sizing: border-box; margin: 0; padding: 0; }
  html, body { width: 1200px; height: 1002px; overflow: hidden; background: var(--stage); }
  .card {
    position: absolute; left: 332px; top: 33px;
    width: 535px; height: 936px;
    background: var(--paper); overflow: hidden;
    font-family: "Arimo", Arial, sans-serif; color: var(--ink);
  }
  .card__swoosh { position: absolute; left: 0; top: 0; }
  .brand {
    position: absolute; left: 95px; top: 105px; width: 440px;
    display: flex; align-items: center; gap: 14px;
    font-family: "EB Garamond", Georgia, serif; font-weight: 600;
    font-size: 36px; color: var(--brown); letter-spacing: 0.5px;
  }
  .brand__mark { width: 22px; height: 22px; background: var(--brown); flex: none; }
  .holder { position: absolute; left: 0; width: 100%; text-align: center; font-family: "EB Garamond", Georgia, serif; }
  .holder__name { top: 240px; font-size: 30px; font-weight: 400; }
  .holder__title { top: 282px; font-size: 24px; font-style: italic; font-weight: 600; color: #222; }
  .info-band {
    position: absolute; left: 0; top: 323px; width: 100%; height: 139px;
    background: var(--band); padding: 6px 18px 0 15px;
    display: flex; justify-content: space-between;
  }
  .info-band h3 { font-family: "EB Garamond", Georgia, serif; font-weight: 700; font-size: 30px; color: var(--brown); line-height: 1.1; margin-bottom: 2px; }
  .info-band p { color: var(--teal-text); font-size: 23px; line-height: 29px; white-space: nowrap; }
  .contacts { text-align: right; }
  .contacts h3 { margin-bottom: -4px; margin-top: -6px; }
  .location { padding-top: 6px; }
  .advisory { position: absolute; left: 0; top: 478px; width: 100%; text-align: center; }
  .advisory h2 { font-family: "EB Garamond", Georgia, serif; font-weight: 600; font-size: 32px; color: var(--ink); margin-bottom: 6px; }
  .advisory p { color: var(--brown); font-size: 23px; line-height: 29px; }
  .affiliations { position: absolute; left: 18px; top: 593px; list-style: none; font-size: 21px; line-height: 29px; color: #333; }
  .affiliations li::before { content: "•"; margin-right: 3px; }
  .social { position: absolute; left: 16px; top: 724px; list-style: none; }
  .social li { display: flex; align-items: center; height: 39px; font-size: 23px; color: #333; }
  .social__bar {
    width: 68px; height: 24px; margin-right: 14px; position: relative;
    background: linear-gradient(90deg, var(--teal-soft), #d7ecee);
  }
  .social__bar::after {
    content: ""; position: absolute; right: -6px; top: 1px; width: 22px; height: 22px;
    border-radius: 50%; background: var(--teal); border: 2px solid #fff;
  }
  .site {
    position: absolute; left: 0; bottom: 0; width: 100%; height: 36px;
    background: var(--footer); color: #fff; text-align: center;
    font-size: 25px; line-height: 36px;
  }
</style>
</head>
<body>
  <article class="card">
    <svg class="card__swoosh" width="330" height="240" viewBox="0 0 330 240" aria-hidden="true">
      <path d="M0 0 H310 C180 25 60 90 0 225 Z" fill="var(--shade)"/>
      <path d="M0 0 H305 C175 20 55 80 0 215 Z" fill="var(--teal)"/>
    </svg>

    <div class="brand"><span class="brand__mark"></span>RJV Wealth Management</div>

    <h1 class="holder holder__name">Gil Prawley</h1>
    <p class="holder holder__title">Registered Representative</p>

    <section class="info-band">
      <div class="location">
        <h3>Location:</h3>
        <p>phe sa;hhe</p>
        <p>ahl alal alal laalla</p>
        <p>allllaalll jfllllllllllllllllllll</p>
      </div>
      <div class="contacts">
        <h3>Contacts:</h3>
        <p>+898 097 76</p>
        <p>Fax: 887f9999a6</p>
        <p>Mobile: 887f9999a6</p>
      </div>
    </section>

    <section class="advisory">
      <h2>Advisory Services</h2>
      <p>offered through Halden Brightwell and</p>
      <p>RBO Registered Investment Advisory Firm.</p>
    </section>

    <ul class="affiliations">
      <li>RJV Wealth Management</li>
      <li>Pelgrave Brokerage(unaffiliated)</li>
      <li>Halden Brightwell (unaffiliated)</li>
      <li>CA Insurance Lic</li>
    </ul>

    <ul class="social">
      <li><span class="social__bar"></span>Pagelink Account HERE</li>
      <li><span class="social__bar"></span>Workconnect Account HERE</li>
      <li><span class="social__bar"></span>Chirper Account HERE</li>
      <li><span class="social__bar"></span>Email Account HERE</li>
    </ul>

    <footer class="site">your website HERE</footer>
  </article>
</body>
</html>
```